Quillfern Nightclub Flyer (Updated)

Flyer for facebook, square is fine, or rectangular. Here is the text:
QUILLFERN
Nightclub + Lounge
presents

SPLIT DECK WEDNESDAY
Nov 29 2018

CLUB FLOOR:
GORDY B2B RALPH
THEODORE BRUSKVIK

LOUNGE:
OTIS B2B HALF TIDE
COPPER FENWICK

Powered by HALVERN Acoustics
4716 Larchmere Avenue 21+ 9pm-2am
quillfernvenue-example.com for VIP booth inquiries

Target Market(s)

Nightclub

Industry/Entity Type

Night Club

Font styles to use
Sans Serif

Colors

Designer to choose colors to be used in the design.

Requirements
Must have
• All the text listed, and plz keep the theme of the attached files. We want to stay consistent with the Quillfern brand
Nice to have
• Try to stay with the theme from the attachments
Should not have
• Dont' stray to far from the general theme we have from the attachments

```html
<!DOCTYPE html>
<html lang="en">
<head>
<meta charset="utf-8">
<title>Quillfern Nightclub – Split Deck Wednesday</title>
<link href="https://fonts.googleapis.com/css2?family=Monoton&family=Montserrat:wght@700;800&family=Questrial&display=swap" rel="stylesheet">
<style>
  :root {
    --gold: #e8df8c;
    --gold-deep: #c9a444;
    --white: #ffffff;
    --navy: #0d1740;
    --blue: #2f5fb8;
    --purple: #5a1f66;
    --black: #05060c;
    --grey: #b9b9b9;
  }
  html, body { margin: 0; padding: 0; overflow: hidden; background: var(--black); }
  .flyer {
    position: relative;
    width: 1200px;
    height: 1200px;
    overflow: hidden;
    background:
      radial-gradient(circle at 50% 52%, #3b6cc4 0%, #1d3a86 28%, transparent 60%),
      radial-gradient(circle at 88% 78%, var(--purple) 0%, transparent 40%),
      linear-gradient(180deg, var(--navy) 0%, #14235e 45%, #0a0f2c 100%);
    font-family: "Questrial", sans-serif;
    color: var(--white);
  }
  .glitter {
    position: absolute; left: 0; top: 0; width: 1200px; height: 330px;
    background: linear-gradient(180deg, #2a1d05 0%, #6b4d12 30%, rgba(150,110,30,0.45) 60%, rgba(20,25,60,0) 100%);
  }
  .crowd {
    position: absolute; left: 0; top: 700px; width: 1200px; height: 500px;
    background: linear-gradient(180deg, rgba(5,6,12,0) 0%, rgba(5,6,12,0.75) 35%, var(--black) 70%);
  }
  .frame { position: absolute; left: 0; top: 0; }
  .title {
    position: absolute; left: 0; width: 1200px; top: 190px;
    text-align: center; font-family: "Monoton", sans-serif;
    font-size: 56px; line-height: 110px; color: var(--gold);
    letter-spacing: -2px; margin: 0; font-weight: 400;
  }
  .date {
    position: absolute; left: 0; width: 1200px; top: 330px;
    text-align: center; font-size: 56px; line-height: 70px;
  }
  .date .time { color: var(--gold); }
  .lineup {
    position: absolute; top: 470px; width: 460px; text-align: center;
  }
  .lineup.club { left: 146px; }
  .lineup.lounge { left: 628px; }
  .lineup h2 {
    margin: 0; font-family: "Montserrat", sans-serif; font-weight: 700;
    font-size: 56px; line-height: 66px; color: var(--gold);
  }
  .lineup p { margin: 0; font-size: 35px; line-height: 43px; }
  .divider { position: absolute; left: 627px; top: 447px; width: 3px; height: 205px; background: var(--gold); }
  .brand {
    position: absolute; left: 54px; top: 940px; width: 300px; text-align: center;
  }
  .brand .dot { width: 110px; height: 110px; border-radius: 50%; background: var(--gold); margin: 0 auto 18px; }
  .brand .name { font-size: 50px; line-height: 54px; letter-spacing: 1px; }
  .brand .sub { font-size: 13px; letter-spacing: 2px; color: var(--grey); margin-top: 6px; }
  .age {
    position: absolute; left: 470px; top: 1036px; width: 160px; text-align: center;
    font-family: "Montserrat", sans-serif; font-weight: 800; font-size: 72px; line-height: 80px;
  }
  .info {
    position: absolute; right: 71px; top: 950px; text-align: right;
  }
  .info p { margin: 0; }
  .info .power { font-size: 33px; line-height: 46px; }
  .info .gold { color: var(--gold); }
  .info .address { font-size: 37px; line-height: 50px; }
  .info .address svg { vertical-align: -2px; margin-right: 14px; }
  .info .web { font-size: 30px; line-height: 34px; margin-top: 8px; }
  .info .web b { font-family: "Montserrat", sans-serif; font-weight: 700; color: var(--gold); }
  .info .vip { font-size: 32px; line-height: 34px; }
</style>
</head>
<body>
<main class="flyer">
  <div class="glitter" role="img" aria-label="Falling gold glitter sparkles across the top"></div>
  <div class="crowd" role="img" aria-label="Silhouetted crowd of dancers with raised hands"></div>

  <svg class="frame" width="1200" height="1200" viewBox="0 0 1200 1200" aria-hidden="true">
    <path d="M51 28 H1157 V57 H1183 V1153 H1157 V1182 H51 V1153 H25 V57 H51 Z" fill="none" stroke="#e8df8c" stroke-width="3"/>
    <path d="M61 38 H1147 V47 H1173 V1163 H1147 V1172 H61 V1163 H35 V47 H61 Z" fill="none" stroke="#c9a444" stroke-width="2"/>
  </svg>

  <h1 class="title">SPLIT DECK WEDNESDAY</h1>
  <div class="date">NOV 29 2018 | <span class="time">9PM-2AM</span></div>

  <section class="lineup club">
    <h2>CLUB FLOOR:</h2>
    <p>GORDY B2B RALPH</p>
    <p>THEODORE BRUSKVIK</p>
  </section>
  <div class="divider"></div>
  <section class="lineup lounge">
    <h2>LOUNGE:</h2>
    <p>OTIS B2B HALF TIDE</p>
    <p>COPPER FENWICK</p>
  </section>

  <div class="brand">
    <div class="dot"></div>
    <div class="name">QUILLFERN</div>
    <div class="sub">NIGHTCLUB + LOUNGE</div>
  </div>

  <div class="age">21+</div>

  <div class="info">
    <p class="power">Powered by <span class="gold">HALVERN Acoustics</span></p>
    <p class="address"><svg width="20" height="28" viewBox="0 0 20 28"><path d="M10 0 C4.5 0 0 4.3 0 9.6 C0 16.8 10 28 10 28 C10 28 20 16.8 20 9.6 C20 4.3 15.5 0 10 0 Z M10 13.5 A4 4 0 1 1 10 5.5 A4 4 0 1 1 10 13.5 Z" fill="#e8df8c"/></svg>4716 Larchmere Avenue</p>
    <p class="web"><b>quillfernvenue-example</b>.com</p>
    <p class="vip">for <span class="gold">VIP booth</span> inquiries</p>
  </div>
</main>
</body>
</html>
```